IT Company based on Biology Business Needs a PowerPoint Design

We need a powerpoint design for a new company called 'Vast KELP'. We develop the machine learning solutions especially focused on deep learning algorithms for biology industry. Our initial product is a vision detection on biological images to help doctors diagnose the symptoms. We would like to see designs that use the color green.

Industry/Entity Type

Biotechnology

Requirements
Nice to have
• Lots of slide templates with company logo's look and feel

```html
<!DOCTYPE html>
<html lang="en">
<head>
<meta charset="utf-8">
<title>Vast KELP – Slide Templates</title>
<link href="https://fonts.googleapis.com/css2?family=Tinos&family=Arimo:wght@400&family=Carlito&display=swap" rel="stylesheet">
<style>
  :root {
    --leaf: rgba(125, 196, 84, 0.88);
    --leaf-solid: #7cc055;
    --forest: #1f8c3f;
    --ink: #151515;
    --white: #ffffff;
    --paper: #ffffff;
    --number: #2e8a47;
    --serif: "Tinos", "Times New Roman", serif;
    --sans: "Arimo", Arial, sans-serif;
    --body: "Carlito", Calibri, sans-serif;
  }
  * { margin: 0; padding: 0; box-sizing: border-box; }
  html, body { width: 1200px; height: 454px; overflow: hidden; background: var(--paper); }
  .canvas { position: relative; width: 1200px; height: 454px; }
  .slide { position: absolute; width: 400px; height: 227px; background: var(--white); overflow: hidden; }
  .abs { position: absolute; }
  .photo { position: absolute; }
  .band { position: absolute; background: var(--leaf); }
  .panel { position: absolute; background: var(--forest); color: var(--white); }
  .heading { font-family: var(--serif); color: var(--ink); text-transform: uppercase; font-weight: 400; line-height: 1.05; letter-spacing: 0.3px; }
  .sub { font-family: var(--sans); font-size: 10.5px; line-height: 1.15; }
  .copy { font-family: var(--body); font-size: 7.6px; line-height: 1.25; }
  .page-no { position: absolute; left: 15px; bottom: 7px; width: 13px; height: 13px; border: 1px solid var(--number); border-radius: 50%;
             font-family: var(--serif); font-size: 7px; color: var(--number); display: flex; align-items: center; justify-content: center; }
  .brand { position: absolute; right: 16px; bottom: 9px; display: flex; align-items: center; gap: 3px;
           font-family: var(--sans); font-size: 7.5px; color: var(--forest); letter-spacing: 0.2px; }
  .brand-dot { width: 7px; height: 7px; border-radius: 50%; background: var(--leaf-solid); }
  .brand.large { right: 12px; bottom: 14px; font-size: 12px; gap: 5px; }
  .brand.large .brand-dot { width: 12px; height: 12px; }
  .bullet { display: flex; gap: 6px; margin-bottom: 7px; }
  .bullet-num { flex: none; width: 9px; height: 9px; border-radius: 50%; background: var(--forest); color: var(--white);
                font-family: var(--sans); font-size: 5.5px; display: flex; align-items: center; justify-content: center; margin-top: 1px; }
  .feature { position: absolute; width: 82px; text-align: center; color: var(--ink); }
  .feature-icon { width: 26px; height: 26px; border-radius: 50%; background: var(--forest); margin: 0 auto 6px; display: flex; align-items: center; justify-content: center; }
  .feature .copy { text-align: left; margin-top: 9px; padding-left: 4px; }
</style>
</head>
<body>
<div class="canvas">

  <!-- Slide 1: title page -->
  <section class="slide" style="left:0;top:0;">
    <div class="photo" role="img" aria-label="Scientist in mask holding a flask of green liquid in a laboratory" style="left:0;top:0;width:400px;height:178px;background:linear-gradient(100deg,#e9ecec 0%,#d8dedd 35%,#f1f1ef 60%,#cfd7d8 100%);"></div>
    <div class="band" style="left:76px;top:0;width:248px;height:138px;"></div>
    <h1 class="heading abs" style="left:76px;top:48px;width:248px;text-align:center;font-size:32px;">Title Page</h1>
    <p class="sub abs" style="left:76px;top:86px;width:248px;text-align:center;font-size:9.5px;color:var(--ink);">Insert Subtitle And Date</p>
    <div class="page-no">1</div>
    <div class="brand large"><span class="brand-dot"></span>VAST KELP</div>
  </section>

  <!-- Slide 2: title with bullets -->
  <section class="slide" style="left:400px;top:0;">
    <div class="photo" role="img" aria-label="Pale green background of microscopic cells" style="left:0;top:0;width:400px;height:196px;background:radial-gradient(circle at 60% 40%,#e4ead9 0%,#d3dcc3 55%,#c4cfb1 100%);"></div>
    <div class="band" style="left:0;top:28px;width:368px;height:60px;"></div>
    <div class="photo" role="img" aria-label="Scientist in a lab coat holding up two sample tubes" style="left:30px;top:10px;width:150px;height:217px;background:linear-gradient(180deg,#b9bdb5 0%,#eef0ee 40%,#f7f7f7 100%);"></div>
    <h2 class="heading abs" style="left:198px;top:36px;font-size:20px;">Insert<br>Title Here</h2>
    <div class="abs" style="left:202px;top:107px;width:190px;color:var(--ink);">
      <div class="bullet"><span class="bullet-num">1</span><p class="copy">Lorem ipsum dolor sit amet, consectetuer adipiscing elit. Maecenas porttitor congue massa.</p></div>
      <div class="bullet"><span class="bullet-num">2</span><p class="copy">Lorem ipsum dolor sit amet, consectetuer adipiscing elit. Maecenas porttitor congue massa.</p></div>
      <div class="bullet"><span class="bullet-num">3</span><p class="copy">Lorem ipsum dolor sit amet, consectetuer adipiscing elit. Maecenas porttitor congue massa.</p></div>
    </div>
    <div class="page-no">2</div>
    <div class="brand"><span class="brand-dot"></span>VAST KELP</div>
  </section>

  <!-- Slide 3: two columns -->
  <section class="slide" style="left:800px;top:0;">
    <div class="photo" role="img" aria-label="Green-tinted laboratory bench with test tubes" style="left:0;top:0;width:400px;height:100px;background:linear-gradient(90deg,#9ccf7f 0%,#86c266 50%,#a3d08a 100%);"></div>
    <div class="panel" style="left:18px;top:100px;width:382px;height:96px;"></div>
    <div class="abs" style="left:200px;top:0;width:1px;height:196px;background:var(--white);"></div>
    <h2 class="heading abs" style="left:66px;top:46px;font-size:18px;text-align:right;width:122px;">Insert<br>Title Here</h2>
    <h2 class="heading abs" style="left:222px;top:46px;font-size:18px;">Insert<br>Title Here</h2>
    <div class="photo" role="img" aria-label="Microscope" style="left:12px;top:98px;width:48px;height:82px;border-radius:6px;background:linear-gradient(180deg,#d9dcdc,#8e9495);"></div>
    <div class="photo" role="img" aria-label="Round flask of blue liquid" style="left:336px;top:96px;width:56px;height:92px;border-radius:28px 28px 28px 28px;background:linear-gradient(180deg,#e8eef2 0%,#e8eef2 35%,#3f8fe0 60%,#1a5fc2 100%);"></div>
    <div class="abs" style="left:70px;top:108px;width:125px;color:var(--white);">
      <p class="sub">Subtitle<br>Information</p>
      <p class="copy" style="margin-top:3px;">Lorem ipsum dolor sit amet, consectetuer adipiscing elit. Maecenas porttitor congue massa. Lorem ipsum dolor sit amet, consectetuer adipiscing elit.</p>
    </div>
    <div class="abs" style="left:223px;top:108px;width:115px;color:var(--white);">
      <p class="sub">Subtitle<br>Information</p>
      <p class="copy" style="margin-top:3px;">Lorem ipsum dolor sit amet, consectetuer adipiscing elit. Maecenas porttitor congue massa. Lorem ipsum dolor sit amet, consectetuer adipiscing elit.</p>
    </div>
    <div class="page-no">3</div>
    <div class="brand"><span class="brand-dot"></span>VAST KELP</div>
  </section>

  <!-- Slide 4: section header -->
  <section class="slide" style="left:0;top:227px;">
    <div class="photo" role="img" aria-label="Scientist with a pipette and blue gloves, blurred laboratory background" style="left:0;top:0;width:400px;height:195px;background:linear-gradient(90deg,#5fb8d6 0%,#9fcfdc 30%,#c9a596 55%,#86b8c4 80%,#4fa4c8 100%);"></div>
    <div class="band" style="left:98px;top:42px;width:204px;height:112px;"></div>
    <h2 class="heading abs" style="left:98px;top:72px;width:204px;text-align:center;font-size:27px;">Section<br>Header</h2>
    <div class="page-no">4</div>
    <div class="brand"><span class="brand-dot"></span>VAST KELP</div>
  </section>

  <!-- Slide 5: header band with two columns -->
  <section class="slide" style="left:400px;top:227px;">
    <div class="photo" role="img" aria-label="Laboratory glassware with blue liquids and test tube racks" style="left:0;top:0;width:400px;height:97px;background:linear-gradient(90deg,#7fa7b5 0%,#3f7fb1 30%,#cfe0e8 55%,#5a97bd 80%,#a9c6d3 100%);"></div>
    <div class="band" style="left:32px;top:65px;width:336px;height:32px;"></div>
    <h2 class="heading abs" style="left:32px;top:74px;width:336px;text-align:center;font-size:16px;">Insert&nbsp; Title Here</h2>
    <div class="panel" style="left:32px;top:97px;width:336px;height:98px;"></div>
    <div class="abs" style="left:50px;top:113px;width:140px;color:var(--white);">
      <p class="sub">Subtitle<br>Information</p>
      <p class="copy" style="margin-top:3px;">Lorem ipsum dolor sit amet, consectetuer adipiscing elit. Maecenas porttitor congue massa. Lorem ipsum dolor sit amet, consectetuer adipiscing elit.</p>
    </div>
    <div class="abs" style="left:219px;top:113px;width:140px;color:var(--white);">
      <p class="sub">Subtitle<br>Information</p>
      <p class="copy" style="margin-top:3px;">Lorem ipsum dolor sit amet, consectetuer adipiscing elit. Maecenas porttitor congue massa. Lorem ipsum dolor sit amet, consectetuer adipiscing elit.</p>
    </div>
    <div class="page-no">5</div>
    <div class="brand"><span class="brand-dot"></span>VAST KELP</div>
  </section>

  <!-- Slide 6: four features -->
  <section class="slide" style="left:800px;top:227px;">
    <div class="photo" role="img" aria-label="Greyscale laboratory scene with sample tubes" style="left:0;top:0;width:400px;height:195px;background:linear-gradient(120deg,#9a9a9a 0%,#c9c9c9 40%,#b1b1b1 70%,#d8d8d8 100%);"></div>
    <div class="band" style="left:32px;top:1px;width:336px;height:38px;"></div>
    <h2 class="heading abs" style="left:32px;top:12px;width:336px;text-align:center;font-size:16px;">Insert&nbsp; Title Here</h2>

    <div class="feature" style="left:15px;top:64px;">
      <div class="feature-icon"><svg width="16" height="16" viewBox="0 0 16 16" fill="none" stroke="#fff" stroke-width="1.4"><path d="M4 14C4 9 12 7 12 2"/><path d="M12 14C12 9 4 7 4 2"/><path d="M5 4h6M5 12h6M6 8h4"/></svg></div>
      <p class="sub">Subtitle<br>Information</p>
      <p class="copy">Lorem ipsum dolor sit amet, consectetuer adipiscing elit. Maecenas porttitor congue massa. consectetuer adipiscing</p>
    </div>
    <div class="feature" style="left:111px;top:64px;">
      <div class="feature-icon"><svg width="16" height="16" viewBox="0 0 16 16" fill="none" stroke="#fff" stroke-width="1.4"><path d="M6 2h4M7 2v5L3 14h10L9 7V2"/><path d="M5 11h6" /></svg></div>
      <p class="sub">Subtitle<br>Information</p>
      <p class="copy">Lorem ipsum dolor sit amet, consectetuer adipiscing elit. Maecenas porttitor congue massa. consectetuer adipiscing</p>
    </div>
    <div class="feature" style="left:207px;top:64px;">
      <div class="feature-icon"><svg width="16" height="16" viewBox="0 0 16 16" fill="#fff"><circle cx="8" cy="5" r="3"/><path d="M2 15c0-4 3-6 6-6s6 2 6 6z"/></svg></div>
      <p class="sub">Subtitle<br>Information</p>
      <p class="copy">Lorem ipsum dolor sit amet, consectetuer adipiscing elit. Maecenas porttitor congue massa. consectetuer adipiscing</p>
    </div>
    <div class="feature" style="left:303px;top:64px;">
      <div class="feature-icon"><svg width="16" height="16" viewBox="0 0 16 16" fill="none" stroke="#fff" stroke-width="1.4"><rect x="2" y="2" width="12" height="12" rx="2"/><path d="M8 5v6M5 8h6" stroke-width="2"/></svg></div>
      <p class="sub">Subtitle<br>Information</p>
      <p class="copy">Lorem ipsum dolor sit amet, consectetuer adipiscing elit. Maecenas porttitor congue massa. consectetuer adipiscing</p>
    </div>
    <div class="page-no">6</div>
    <div class="brand"><span class="brand-dot"></span>VAST KELP</div>
  </section>

</div>
</body>
</html>
```